Boat Charter Power Point Template

Power Point Template for a Catalogue for a Boat Charter Company. In each slide there will be a main foto of the boat and then 3 mini photos plus all the aditional information of each boat. Here I attach 2 diferent presentations to get inspired

```html
<!DOCTYPE html>
<html lang="en">
<head>
<meta charset="utf-8">
<title>Boat Charter Catalogue Template</title>
<link href="https://fonts.googleapis.com/css2?family=Playfair+Display:wght@400;700&family=Lato:wght@400;700&display=swap" rel="stylesheet">
<style>
:root{
  --canvas:#4a4a4a;
  --white:#ffffff;
  --ink:#1c1c1c;
  --muted:#6f6f6f;
  --gold:#c49a1e;
  --panel-dark:#1d1d1d;
  --sky-top:#c9dbe9;
  --sky-low:#9fc0d8;
  --sea:#2c6f9c;
  --sea-deep:#17476b;
  --teal:#1d8c93;
  --pale-blue:#dfe6f2;
}
*{margin:0;padding:0;box-sizing:border-box}
html,body{width:750px;height:1200px;overflow:hidden}
body{background:var(--canvas);font-family:'Lato',sans-serif;color:var(--ink);position:relative}
.slide{position:absolute;left:117px;width:600px;background:var(--white);overflow:hidden}
.abs{position:absolute}
.tiny{font-size:6px;line-height:1.5;color:var(--muted)}
.label{font-family:'Playfair Display',serif;font-weight:700;font-size:11px;color:var(--ink)}

/* slide 1 (cropped) */
.s-top{top:0;height:50px}
.s-top .photo{left:0;top:0;width:320px;height:50px;background:linear-gradient(90deg,#1f3f5e,#3a6a8f 60%,#b8c9d6)}
.s-top .cta{right:18px;top:22px;width:40px;height:14px;border:1px solid #bbb;font-size:5px;text-align:center;line-height:12px;color:var(--muted)}

/* slide 2: cover */
.s-cover{top:57px;height:338px}
.s-cover .photo{left:0;top:0;width:600px;height:338px;background:linear-gradient(180deg,var(--sky-top) 0%,var(--sky-low) 62%,var(--sea) 80%,var(--sea-deep) 100%)}
.cover-box{left:37px;top:48px;width:233px;height:290px;background:var(--panel-dark);padding:22px 20px}
.cover-box .section{font-size:7px;letter-spacing:2px;color:var(--gold);text-align:right}
.cover-box h1{font-family:'Playfair Display',serif;font-weight:700;font-size:26px;line-height:1.15;color:var(--white);margin-top:8px;letter-spacing:1px}
.cover-box .sub{font-family:'Playfair Display',serif;font-size:10px;color:#d8cfa8;margin-top:56px}
.cover-box .tiny{color:#9a9a9a;margin-top:70px;width:130px}

/* slide 3: boat detail */
.s-detail{top:400px;height:332px}
.s-detail .photo{left:0;top:0;width:395px;height:332px;background:linear-gradient(180deg,#d7e7f2 0%,#e9eef2 35%,#3fb2c6 58%,#1f7aa0 100%)}
.s-detail h2{left:412px;top:62px;width:160px;font-family:'Playfair Display',serif;font-weight:700;font-size:18px;line-height:1.2;color:var(--ink);white-space:nowrap}
.bullets{left:418px;top:102px;list-style:none}
.bullets li{font-size:6px;color:var(--muted);margin-bottom:8px;position:relative;padding-left:10px;line-height:1.4}
.bullets li::before{content:"";position:absolute;left:0;top:2px;width:5px;height:5px;border-radius:50%;background:var(--gold)}
.bullets li b{color:var(--gold);font-weight:400;display:block}
.specs{left:418px;top:210px;width:140px}
.specs .row{display:flex;justify-content:space-between;font-size:7px;margin-bottom:9px;color:var(--ink)}
.specs .row span:last-child{color:var(--gold)}
.specs .tiny{margin-top:-5px}
.s-detail .vert{right:6px;top:70px;writing-mode:vertical-rl;font-size:5px;letter-spacing:1px;color:var(--muted)}
.s-detail .page{right:10px;bottom:10px;font-size:7px;font-weight:700}

/* slide 4: grid */
.s-grid{top:740px;height:340px}
.cell{position:absolute;width:278px;height:113px}
.cell.text{padding:16px 18px}
.cell.text .label{margin-bottom:8px;display:block}
.cols{display:flex;gap:14px}
.img-interior{background:linear-gradient(160deg,#f1ede6,#cfc6b8)}
.img-aerial{background:linear-gradient(135deg,#2aa3a6,var(--teal) 45%,#0f5f6a)}
.img-deck{background:linear-gradient(160deg,#efe6d8,#b79f80)}
.gold-strip{right:0;top:0;width:40px;height:340px;background:var(--gold)}
.gold-strip .shade{position:absolute;left:0;top:135px;width:40px;height:205px;background:#b5b5b5}

/* slide 5 (cropped) */
.s-intro{top:1087px;height:113px}
.s-intro .photo{left:0;top:0;width:195px;height:113px;background:linear-gradient(180deg,#3c6f98,#1d4768)}
.s-intro h3{left:200px;top:18px;font-family:'Playfair Display',serif;font-weight:700;font-size:15px}
.s-intro .tiny{left:200px;top:42px;width:150px}
.s-intro .note{left:475px;top:0;width:105px;height:113px;background:var(--pale-blue);padding:44px 10px}
</style>
</head>
<body>

<section class="slide s-top">
  <div class="abs photo" role="img" aria-label="Photo of a skipper at the helm of a yacht"></div>
  <p class="abs tiny" style="left:340px;top:6px;width:110px">Crew of four, chef on board and daily housekeeping.</p>
  <p class="abs tiny" style="left:465px;top:6px;width:100px">Water toys and tender included on request.</p>
  <div class="abs cta">More</div>
</section>

<section class="slide s-cover">
  <div class="abs photo" role="img" aria-label="Photo of a white motor yacht on calm sea under a pale sky"></div>
  <div class="abs cover-box">
    <p class="section">SECTION 01</p>
    <h1>BOAT/OFFER<br>TITLE</h1>
    <p class="sub">Title SubHeading</p>
    <p class="tiny">Short text about this charter offer, its route, season and the main highlights of the boat.</p>
  </div>
</section>

<section class="slide s-detail">
  <div class="abs photo" role="img" aria-label="Photo of a large white yacht on turquoise water"></div>
  <h2 class="abs">Slide Title Here</h2>
  <ul class="abs bullets">
    <li>Eight Guests Cruising<b>Four cabins</b></li>
    <li>Full Crew &amp; Captain<b>Chef included</b></li>
    <li>Long Range Cruises<b>Med waters</b></li>
  </ul>
  <div class="abs specs">
    <div class="row"><span>Capacity</span><span>10 Guests</span></div>
    <div class="row"><span>Fuel Tes</span><span>3000 L</span></div>
    <div class="row"><span>Length Boat</span><span>32 m</span></div>
    <div class="row"><span>Included</span><span></span></div>
    <p class="tiny">Towels, linen, snorkel gear and tender.</p>
  </div>
  <p class="abs vert">Boat Charter Catalogue 2024</p>
  <p class="abs page">06</p>
</section>

<section class="slide s-grid">
  <div class="cell img-interior" style="left:0;top:0" role="img" aria-label="Photo of a yacht lounge interior"></div>
  <div class="cell text" style="left:278px;top:0">
    <span class="label">Accommodation</span>
    <div class="cols"><p class="tiny">Four cabins with private bathrooms and sea views.</p><p class="tiny">Master suite on main deck with lounge area.</p></div>
  </div>
  <div class="cell text" style="left:0;top:113px">
    <span class="label">Inclusions</span>
    <div class="cols"><p class="tiny">Crew, fuel for daily cruising and welcome drinks.</p><p class="tiny">Port fees and full linen service on board.</p></div>
  </div>
  <div class="cell img-aerial" style="left:278px;top:113px" role="img" aria-label="Aerial photo of a yacht on teal water"></div>
  <div class="cell img-deck" style="left:0;top:226px;height:114px" role="img" aria-label="Photo of a sun deck with loungers"></div>
  <div class="cell text" style="left:278px;top:226px">
    <span class="label">Equipments</span>
    <div class="cols"><p class="tiny">Jet ski, paddle boards and snorkel kits.</p><p class="tiny">Wifi, sound system and outdoor cinema.</p></div>
  </div>
  <div class="abs gold-strip"><div class="shade"></div></div>
</section>

<section class="slide s-intro">
  <div class="abs photo" role="img" aria-label="Photo of a yacht on deep blue sea"></div>
  <h3 class="abs">Intro Boat Line</h3>
  <p class="abs tiny">A short introduction to this boat line, its style, comfort and the charter areas it covers each season.</p>
  <div class="abs note"><p class="tiny">Ask our team for season rates.</p></div>
</section>

</body>
</html>
```